House Cleaning company in need of handout re-designs

We are looking to create a 2 sided, full color, 6" x 4" handout that promotes the company www.dustly.com

We have one in existence that performed well, but find it too busy and would like another one designed to test performance (please see the attached files for original design). We are looking for one additional design, however depending on quality of work submitted we will select up to 5 designs.

We are looking for clean designs the will improve performance and you are 'carte blanche' on the design. That said, please ensure the following elements are present:

1) Space for an offer (i.e $39 for 3 hours of cleaning) with an expiry date.
2) Unique URL
3) Promo Code
4) Phone Number
5) The tagline of "Let Dustly handle it" is present.
6) Logo
7) Brand colors are maintained

Also, please highlight the following:

*Eco-Friendly Cleaning Services
*Fully-Screened Cleaning Experts
*60-point checklist
*Easy Online Booking Process

Thank you.

House Cleaning

```html
<!DOCTYPE html>
<html lang="en">
<head>
<meta charset="utf-8">
<title>Dustly – Handout</title>
<link rel="stylesheet" href="https://fonts.googleapis.com/css2?family=Questrial&family=Roboto+Condensed:wght@400;700&family=Oswald:wght@500&family=Arimo:wght@400;700&display=swap">
<style>
:root{
  --green:#2f7d12;
  --green-light:#5aa51d;
  --green-dark:#1f5c0a;
  --orange:#e08a1c;
  --orange-dark:#c86f0e;
  --amber:#f6a61e;
  --rose:#d9666a;
  --charcoal:#4a4a4a;
  --paper:#eeeeee;
  --cream:#fff6dc;
  --white:#ffffff;
}
*{margin:0;padding:0;box-sizing:border-box}
html,body{width:841px;height:1200px;overflow:hidden;background:var(--white)}
.sheet{position:relative;width:841px;height:1200px;font-family:"Arimo",sans-serif}
.card{position:absolute;left:0;width:841px;height:600px;overflow:hidden}
.card--front{top:0;background:linear-gradient(180deg,#f4f4f4,var(--paper))}
.card--back{top:600px;background:linear-gradient(180deg,#fff 0%,var(--cream) 45%,#ffe6a8 100%);border-top:3px solid var(--white)}
.swoosh{position:absolute;inset:0}
.photo{position:absolute}
.photo--man{left:0;top:0;width:365px;height:600px;background:linear-gradient(170deg,#d7d2c8 0%,#e9e1d2 30%,#2f6a2e 60%,#1f4d22 100%)}
.photo--woman{left:0;top:95px;width:285px;height:505px;background:linear-gradient(170deg,#f2e3cc 0%,#f8e9c3 35%,#f4c43e 70%,#eeb526 100%)}
.rule-dots{position:absolute;height:0;border-top:3px dotted var(--green)}
.headline{position:absolute;left:340px;width:480px;text-align:center}
.headline__lead{font-family:"Questrial",sans-serif;color:var(--green);font-size:47px;line-height:1}
.headline__mid{font-family:"Questrial",sans-serif;color:var(--green);font-size:38px;line-height:1;margin-top:4px}
.headline__mid b{font-family:"Arimo",sans-serif}
.headline__big{font-family:"Roboto Condensed",sans-serif;font-weight:700;color:var(--orange);font-size:66px;line-height:1;margin-top:2px}
.perks{position:absolute;list-style:none}
.perks li{position:relative;padding-left:26px}
.perks li::before{content:"•";position:absolute;left:0}
.perks b{font-weight:700}
.perks--front{left:418px;top:258px;color:var(--white);font-size:19px;line-height:22px}
.perks--back{left:312px;top:762px;color:var(--green);font-size:23px;line-height:27px;top:162px}
.book-front{position:absolute;left:438px;top:372px;font-family:"Questrial",sans-serif;font-size:46px;color:var(--white)}
.bar{position:absolute;right:0;color:var(--white);display:flex;align-items:center;justify-content:center}
.bar--url{left:450px;top:423px;height:36px;background:var(--charcoal);font-family:"Roboto Condensed",sans-serif;font-size:29px}
.bar--phone{left:530px;top:460px;height:36px;background:var(--amber);font-family:"Roboto Condensed",sans-serif;font-size:27px;justify-content:flex-start;padding-left:18px}
.brand-box{position:absolute;left:432px;top:500px;width:328px;height:80px;border-left:2px solid #e0c070;border-bottom:2px solid #e0c070}
.brand{font-family:"Roboto Condensed",sans-serif;font-weight:700;color:var(--rose);white-space:nowrap}
.brand--front{position:absolute;left:40px;top:6px;font-size:56px}
.brand--back{position:absolute;left:40px;top:38px;font-size:52px}
.badge{position:absolute;width:200px;height:200px}
.badge__ray{position:absolute;left:30px;top:30px;width:140px;height:140px;background:var(--orange);border-radius:10px}
.badge__ray:nth-child(2){transform:rotate(30deg)}
.badge__ray:nth-child(3){transform:rotate(60deg)}
.badge__ring{position:absolute;left:24px;top:24px;width:152px;height:152px;border-radius:50%;border:2px dashed #f8d08a}
.badge__text{position:absolute;inset:0;display:flex;flex-direction:column;align-items:center;justify-content:center;color:var(--white);font-family:"Roboto Condensed",sans-serif;text-align:center;line-height:1}
.badge__price{font-weight:700;font-size:52px}
.badge__price sup{font-size:26px;vertical-align:top;position:relative;top:6px}
.badge__what{font-size:19px;margin-top:2px}
.badge__end{font-size:13px;margin-top:6px}
.badge--front{left:226px;top:374px}
.badge--back{left:614px;top:403px}
.tagline{position:absolute;left:305px;top:60px;font-family:"Roboto Condensed",sans-serif;font-weight:700;color:var(--green);font-size:43px}
.divider{position:absolute;left:288px;width:440px;border-top:1px solid #c8b38a}
.checks{position:absolute;left:330px;top:300px;list-style:none;font-family:"Oswald",sans-serif;color:var(--green);font-size:20px;line-height:28px;text-transform:uppercase}
.checks li{display:flex;align-items:center;gap:10px}
.checks svg{width:20px;height:20px}
.book-band{position:absolute;left:220px;top:416px;right:0;height:146px;background:linear-gradient(180deg,var(--green-light),var(--green));border-top:3px dotted #bfe39a;border-bottom:3px dotted #bfe39a}
.book-band__inner{position:absolute;left:30px;top:8px;width:345px;text-align:center;color:var(--white)}
.book-band__cta{font-family:"Arimo",sans-serif;font-weight:700;font-size:30px}
.book-band__cta span{color:#f6d35a}
.book-band__url{font-family:"Roboto Condensed",sans-serif;font-size:33px;border-top:1px solid #f6d35a;border-bottom:1px solid #f6d35a;margin-top:2px}
.book-band__phone{font-family:"Roboto Condensed",sans-serif;font-size:36px;margin-top:2px}
</style>
</head>
<body>
<main class="sheet">

  <section class="card card--front">
    <svg class="swoosh" viewBox="0 0 841 600" aria-hidden="true">
      <path d="M0 330 C250 300 520 190 841 205 L841 232 C540 222 300 330 0 360 Z" fill="#c9a34a" opacity=".6"/>
      <path d="M0 350 C260 330 520 222 841 232 L841 410 C600 420 330 500 0 560 Z" fill="#3f8d16"/>
      <path d="M420 300 C600 240 720 236 841 240 L841 330 C700 320 560 330 420 360 Z" fill="#5aa51d" opacity=".5"/>
    </svg>
    <div class="photo photo--man" role="img" aria-label="Photo of a smiling cleaner in a green apron holding a broom and dustpan"></div>
    <div class="rule-dots" style="left:390px;top:44px;width:410px"></div>
    <div class="headline" style="top:58px">
      <div class="headline__lead">Do You Really Have</div>
      <div class="headline__mid">The <b>time to tackle</b></div>
      <div class="headline__big">HOUSE CHORES?</div>
    </div>
    <ul class="perks perks--front">
      <li><b>Eco-Friendly</b> Cleaning Services</li>
      <li>Fully-Screened <b>Cleaning Experts</b></li>
      <li><b>60-point</b> checklist</li>
      <li>Easy <b>Online Booking</b> Process</li>
    </ul>
    <div class="book-front">Book Now at</div>
    <div class="bar bar--url">www.dustly.com/ca39</div>
    <div class="bar bar--phone">1-800-4DUSTLY</div>
    <div class="brand-box"><span class="brand brand--front">Dustly.com</span></div>
    <div class="badge badge--front">
      <div class="badge__ray"></div><div class="badge__ray"></div><div class="badge__ray"></div>
      <div class="badge__ring"></div>
      <div class="badge__text">
        <div class="badge__price"><sup>$</sup>39</div>
        <div class="badge__what">CLEANING FOR<br>3 HOURS</div>
        <div class="badge__end">Offer Ends 11/30/2014</div>
      </div>
    </div>
  </section>

  <section class="card card--back">
    <span class="brand brand--back">Dustly.com</span>
    <h1 class="tagline">Let Dustly handle it!</h1>
    <div class="photo photo--woman" role="img" aria-label="Photo of a smiling cleaner in a yellow apron holding a spray bottle and sponge"></div>
    <ul class="perks perks--back">
      <li><b>Eco-Friendly</b> Cleaning Services</li>
      <li>Fully-Screened <b>Cleaning Experts</b></li>
      <li><b>60-point</b> checklist</li>
      <li>Easy <b>Online Booking</b> Process</li>
    </ul>
    <div class="divider" style="top:285px"></div>
    <ul class="checks">
      <li><svg viewBox="0 0 20 20"><circle cx="10" cy="10" r="9" fill="#7cbf3a"/><path d="M5.5 10.5l3 3 6-6" stroke="#fff" stroke-width="2.2" fill="none"/></svg>Book a cleaner online for fast, quick service</li>
      <li><svg viewBox="0 0 20 20"><circle cx="10" cy="10" r="9" fill="#7cbf3a"/><path d="M5.5 10.5l3 3 6-6" stroke="#fff" stroke-width="2.2" fill="none"/></svg>Give your home a fresh, through cleaning</li>
      <li><svg viewBox="0 0 20 20"><circle cx="10" cy="10" r="9" fill="#7cbf3a"/><path d="M5.5 10.5l3 3 6-6" stroke="#fff" stroke-width="2.2" fill="none"/></svg>End housework and enjoy more free time</li>
    </ul>
    <div class="book-band">
      <div class="book-band__inner">
        <div class="book-band__cta">::: BOOK NOW <span>at</span> :::</div>
        <div class="book-band__url">www.dustly.com/ca39</div>
        <div class="book-band__phone">1-800-4DUSTLY</div>
      </div>
    </div>
    <div class="badge badge--back">
      <div class="badge__ray"></div><div class="badge__ray"></div><div class="badge__ray"></div>
      <div class="badge__ring"></div>
      <div class="badge__text">
        <div class="badge__price"><sup>$</sup>39</div>
        <div class="badge__what">CLEANING FOR<br>3 HOURS</div>
        <div class="badge__end">Offer Ends 11/30/2014</div>
      </div>
    </div>
  </section>

</main>
</body>
</html>
```